Stationery Refresh For Local Mortgage Broker

We want to modernise and standardise our stationery, including: letterhead, presentation folder, email signature and business card.

The new stationery should be a more modern and professional take on our existing colour scheme and brand. (We do not want a complete overhaul.) A folder of approved stock photos can be found here: https://filebox.example-share.net/f/7kQzR2mTn4vWx9Lp3Yb8-HsdJe5Uc1Ga/view

Our current website is: www.brindlecovefin.com.au but we will be updating this to be consistent with our new stationery.

We are open to *very slight* tweaks to our logo if you feel it needs modernising, but overall we would like to maintain consistent colour scheme.

> Letterhead

148 Calloway Parade,
Harwood, VIC, 3341
ABN: 31 805 249 067
Australian Credit License: 718293

(03) 5391 6084
www.brindlecovefin.com.au

> Presentation Folder

148 Calloway Parade,
Harwood, VIC, 3341
(03) 5391 6084
www.brindlecovefin.com.au

ABN: 31 805 249 067

> Email Signature

Liam Tresidder
Director
M. 0412 857 294
P. (03) 5391 6084
www.brindlecovefin.com.au
148 Calloway Parade,
Harwood, VIC, 3341

ABN: 31 805 249 067

(you can also include a photo if you like: https://brindlecovefin.com.au/wp-content/uploads/2020/12/Liam-Tresidder.png.webp)

> Business Card

Liam Tresidder
Director
M. 0412 857 294
P. (03) 5391 6084
www.brindlecovefin.com.au
148 Calloway Parade,
Harwood, VIC, 3341

ABN: 31 805 249 067

Additional information...

If it's useful/relevant, the services we offer are: Home Loans, Investment Loans, Refinance, Debt Consolidation, Commercial Finance, Vehicle Loans
(You may choose to use this in any of the designs)

Target Market(s)

Home Buyers and Investors

Industry/Entity Type

Mortgage broking/property/real estate

Requirements
Must have
• At least somewhat consistent with our current site (yet meaningfully modernized)
Should not have
• dramatically different logo or colourscheme overhauls

```html
<!DOCTYPE html>
<html lang="en">
<head>
<meta charset="utf-8">
<title>Brindle Cove Financial Services – Stationery</title>
<link rel="stylesheet" href="https://fonts.googleapis.com/css2?family=Montserrat:wght@400;500&family=Didact+Gothic&display=swap">
<style>
  :root{
    --brand-red:#9b0a10;
    --charcoal:#505052;
    --ink:#4a4a4c;
    --canvas-bg:#dcd8d7;
    --panel-grey:#b9b7b8;
    --scene-grey:#cfcfcf;
    --paper:#f2f2f2;
    --white:#ffffff;
  }
  *{box-sizing:border-box;margin:0;padding:0}
  html,body{width:1200px;height:795px;overflow:hidden}
  body{background:var(--canvas-bg);position:relative;font-family:"Montserrat",sans-serif;color:var(--ink)}
  .abs{position:absolute}
  .icon{width:8px;height:8px;fill:var(--brand-red);flex:none}

  .wordmark{display:flex;align-items:center;gap:.45em;font-family:"Montserrat",sans-serif;font-weight:500;color:var(--brand-red);white-space:nowrap;line-height:1;letter-spacing:0}
  .wordmark__mark{width:.7em;height:.7em;background:currentColor;flex:none}

  .contact-list{list-style:none}
  .contact-list li{display:flex;align-items:flex-start;gap:5px;white-space:nowrap}
  .contact-list li .icon{margin-top:2px}

  /* Business cards */
  .card-stage{left:67px;top:81px;width:533px;height:354px;background:var(--scene-grey)}
  .card{width:238px;height:142px;border-radius:9px;overflow:hidden;box-shadow:0 4px 10px rgba(0,0,0,.18)}
  .card--front{left:22px;top:106px;background:var(--white)}
  .card--back{left:273px;top:106px;background:var(--brand-red)}
  .card--front .wordmark{right:16px;top:20px;font-size:10px}
  .card__name{left:16px;top:56px;font-size:9px;color:var(--brand-red);letter-spacing:.5px;text-transform:uppercase}
  .card__role{left:16px;top:68px;font-size:5.5px;color:var(--charcoal)}
  .card__contacts{left:16px;top:84px;font-size:6px;line-height:8.5px;color:var(--ink)}
  .card__contacts .icon{width:5px;height:5px;margin-top:1.8px}
  .card__edge{left:0;bottom:0;width:100%;height:4px;background:var(--brand-red)}
  .card--back .wordmark{left:0;width:100%;justify-content:center;top:56px;font-size:14px;color:var(--white)}
  .card__web{left:0;width:100%;text-align:center;bottom:20px;font-size:6px;letter-spacing:3px;color:var(--white);text-transform:uppercase}

  /* Email signature */
  .signature-panel{left:67px;top:480px;width:546px;height:249px;background:var(--panel-grey)}
  .signature{left:24px;top:23px;width:504px;height:185px;background:var(--paper);overflow:hidden}
  .signature__photo{left:-2px;top:25px;width:156px;height:160px;background:linear-gradient(180deg,#f0eef0 0%,#c9c6cc 55%,#9d9a9f 100%)}
  .signature .wordmark{left:174px;top:52px;font-size:18px}
  .signature__contacts{left:178px;top:101px;font-size:9px;line-height:11.5px;color:var(--ink)}
  .signature__bar{left:154px;bottom:0;width:350px;height:11px}
  .signature__caption{left:0;width:100%;text-align:center;top:231px;font-size:8.5px;color:#222;padding-right:18px}

  /* Letterhead */
  .letterhead{left:656px;top:81px;width:484px;height:678px;background:var(--paper);box-shadow:0 6px 18px rgba(0,0,0,.25);overflow:hidden}
  .letterhead .wordmark{left:42px;top:58px;font-size:14px}
  .letterhead__contacts{left:316px;top:42px;font-size:9.5px;line-height:11.9px;color:var(--ink)}
  .letter{left:42px;top:222px;width:402px;font-family:"Didact Gothic",sans-serif;color:var(--ink)}
  .letter__salutation{font-size:12.5px;margin-bottom:22px}
  .letter p{font-size:7.4px;line-height:10.4px;margin-bottom:10.4px;text-align:left}
  .letter__closing{font-size:7.4px;margin-top:10px}
  .letter__signature{width:58px;height:24px;margin-top:16px;background:linear-gradient(90deg,rgba(40,44,60,.15),rgba(40,44,60,.3),rgba(40,44,60,.1))}
  .letterhead__bar{left:0;bottom:0;width:484px;height:8px}
</style>
</head>
<body>

<svg width="0" height="0" style="position:absolute" aria-hidden="true">
  <symbol id="i-phone" viewBox="0 0 10 10"><path d="M2.2 0.6 3.9 2.6 3 3.9c.6 1.3 1.7 2.4 3 3l1.3-.9 2 1.7-1 1.6C4.5 9.2.8 5.5.6 1.6z"/></symbol>
  <symbol id="i-mobile" viewBox="0 0 10 10"><path d="M2.5 0h5v10h-5zM3.5 1.2v6.6h3V1.2zM4.5 8.4h1v.8h-1z" fill-rule="evenodd"/></symbol>
  <symbol id="i-mail" viewBox="0 0 10 10"><path d="M0 2h10v6H0zM.8 2.8 5 5.8l4.2-3z"/></symbol>
  <symbol id="i-globe" viewBox="0 0 10 10"><path d="M5 0a5 5 0 1 0 0 10A5 5 0 0 0 5 0zM3 2.2l1.8.6.4 1.6-1.6.8L2.4 6 1.4 4.2zM6.4 6.2l1.8-.4-.6 2-1.6.8z" fill-rule="evenodd"/></symbol>
  <symbol id="i-pin" viewBox="0 0 10 10"><path d="M5 0C3 0 1.6 1.5 1.6 3.4 1.6 6 5 10 5 10s3.4-4 3.4-6.6C8.4 1.5 7 0 5 0zm0 2a1.5 1.5 0 1 1 0 3 1.5 1.5 0 0 1 0-3z" fill-rule="evenodd"/></symbol>
</svg>

<section class="card-stage abs" aria-label="Business card, front and back">
  <article class="card card--front abs">
    <div class="wordmark abs"><span class="wordmark__mark"></span>Brindle Cove Financial Services</div>
    <div class="card__name abs">Liam Tresidder</div>
    <div class="card__role abs">Director</div>
    <ul class="contact-list card__contacts abs">
      <li><svg class="icon"><use href="#i-phone"/></svg>(03) 5391 6084</li>
      <li><svg class="icon"><use href="#i-mobile"/></svg>0412 857 294</li>
      <li><svg class="icon"><use href="#i-mail"/></svg>liam@brindlecovefin.com.au</li>
      <li><svg class="icon"><use href="#i-globe"/></svg>brindlecovefin.com.au</li>
      <li><svg class="icon"><use href="#i-pin"/></svg>148 Calloway Parade, Harwood, VIC, 3341</li>
    </ul>
    <div class="card__edge abs"></div>
  </article>
  <article class="card card--back abs">
    <div class="wordmark abs"><span class="wordmark__mark"></span>Brindle Cove Financial Services</div>
    <div class="card__web abs">www.brindlecovefin.com.au</div>
  </article>
</section>

<section class="signature-panel abs" aria-label="Email signature">
  <div class="signature abs">
    <div class="signature__photo abs" role="img" aria-label="Portrait photo of Liam Tresidder in a grey blazer"></div>
    <div class="wordmark abs"><span class="wordmark__mark"></span>Brindle Cove Financial Services</div>
    <ul class="contact-list signature__contacts abs">
      <li><svg class="icon"><use href="#i-mail"/></svg>liam@brindlecovefin.com.au</li>
      <li><svg class="icon"><use href="#i-globe"/></svg>brindlecovefin.com.au</li>
      <li><svg class="icon"><use href="#i-pin"/></svg>148 Calloway Parade<br>Harwood, VIC, 3341</li>
    </ul>
    <svg class="signature__bar abs" viewBox="0 0 350 11" preserveAspectRatio="none" aria-hidden="true">
      <polygon points="0,0 226,0 220,11 0,11" fill="var(--brand-red)"/>
      <polygon points="230,0 350,0 350,11 224,11" fill="var(--charcoal)"/>
    </svg>
  </div>
  <div class="signature__caption abs">EMAILSIGNATURE 01</div>
</section>

<section class="letterhead abs" aria-label="Letterhead">
  <div class="wordmark abs"><span class="wordmark__mark"></span>Brindle Cove Financial Services</div>
  <ul class="contact-list letterhead__contacts abs">
    <li><svg class="icon"><use href="#i-phone"/></svg>(03) 5391 6084</li>
    <li><svg class="icon"><use href="#i-mobile"/></svg>0412 857 294</li>
    <li><svg class="icon"><use href="#i-mail"/></svg>liam@brindlecovefin.com.au</li>
    <li><svg class="icon"><use href="#i-globe"/></svg>brindlecovefin.com.au</li>
    <li><svg class="icon"><use href="#i-pin"/></svg>148 Calloway Parade<br>Harwood, VIC, 3341</li>
  </ul>
  <div class="letter abs">
    <div class="letter__salutation">Dear Mr. Hartley,</div>
    <p>Lorem ipsum dolor sit amet, consectetur adipiscing elit. Donec orci purus, luctus vitae dignissim eu, iaculis sed purus. Vivamus faucibus, ipsum nec aliquet viverra, leo mauris condimentum ligula, sit amet sagittis enim ligula quis arcu. Nam egestas tortor id nisi porttitor mattis. In tortor ante, ultricies in suscipit a, tempus non massa. Vivamus et auctor mi. Fusce vel massa nulla. Phasellus nec eros mauris, et scelerisque orci.</p>
    <p>Donec malesuada orci vitae nulla accumsan porta a id massa. Quisque accumsan iaculis magna sit amet fringilla. Maecenas consequat, magna eget tincidunt semper, odio nibh rutrum mi, id feugiat ante nisi eu risus. Vestibulum nunc orci, rhoncus a placerat in, ultricies in mi. Cras mattis varius eros, vel fringilla nisi suscipit eget. Quisque scelerisque sagittis nulla at porttitor.</p>
    <p>Sed id augue vitae urna euismod commodo aliquet a quam. Pellentesque arcu velit, cursus et malesuada ut, consequat et diam. Nullam erat sem, rhoncus id ullamcorper vitae, rhoncus et arcu. In ultricies ultricies nulla, ut rutrum nisi iaculis at. Donec eu magna a metus ornare faucibus. Fusce aliquet faucibus ultricies. Morbi semper, est id tincidunt gravida, sem arcu adipiscing lacus, ac bibendum nulla leo eu purus. Quisque nec diam sed risus consectetur a ccumsan quis quis nibh. Vestibulum id purus lorem.</p>
    <p>It is a long established fact that a reader will be distracted by the readable content of a page when looking at its layout. The point of using Lorem Ipsum is that it has a more-or-less normal distribution of letters, as opposed to using 'Content here, content here', making it look like readable English. Many desktop publishing packages</p>
    <div class="letter__closing">Sincerely,</div>
    <div class="letter__signature" role="img" aria-label="Handwritten signature"></div>
  </div>
  <svg class="letterhead__bar abs" viewBox="0 0 484 8" preserveAspectRatio="none" aria-hidden="true">
    <polygon points="0,0 370,0 367,8 0,8" fill="var(--brand-red)"/>
    <polygon points="374,0 484,0 484,8 370,8" fill="var(--charcoal)"/>
  </svg>
</section>

</body>
</html>
```